Brookhaven Kitchens Stationary
Stationary Set with Business Card
Project: Brookhaven Kitchens Stationary
Brookhaven Kitchens Stationary - Chef / Catering
Creative Brief
Professional
Daniel Hensley
Chef/Owner
4738 W. Marlow Ave Orlando, FL 32899
dan@brookhavenkitchens.example
www.brookhavenkitchens.example
Simple with the BK (circle) part of the logo on the back, like a branding iron

```html
<!DOCTYPE html>
<html lang="en">
<head>
<meta charset="utf-8">
<title>Brookhaven Kitchens Stationery</title>
<link href="https://fonts.googleapis.com/css2?family=Lato:wght@400;700&display=swap" rel="stylesheet">
<style>
:root{
  --bg:#ece6dc;
  --paper:#ffffff;
  --charcoal:#3b3836;
  --rust:#b0573a;
  --beige:#d7cdbd;
  --ink:#5a5450;
  --faint:#efe7e2;
  --light:#f4ece4;
  --shadow:0 2px 5px rgba(0,0,0,.25);
}
*{box-sizing:border-box;margin:0;padding:0}
html,body{width:1200px;height:310px;overflow:hidden;background:var(--bg);font-family:"Lato",sans-serif;color:var(--ink)}
.canvas{position:relative;width:1200px;height:310px}
.abs{position:absolute}
.brand{display:flex;align-items:center;gap:6px;font-weight:700;color:var(--rust);white-space:nowrap}
.brand .dot{border-radius:50%;background:var(--rust);flex:none}
.brand.light{color:var(--light)}
.brand.light .dot{background:var(--light)}

/* logo block */
.logo-block{left:24px;top:14px;width:216px;text-align:center}
.logo-block .brand{justify-content:center;font-size:22px}
.logo-block .brand .dot{width:14px;height:14px}
.logo-block .tagline{font-size:8px;letter-spacing:1px;color:var(--ink);margin-top:4px}

/* business cards */
.card{width:106px;height:72px;box-shadow:var(--shadow);overflow:hidden}
.card-dark{background:var(--charcoal);color:#ddd}
.card-rust{background:var(--rust)}
.card .band{position:absolute;left:0;right:0;top:30px;height:12px;background:var(--rust)}
.card .name{position:absolute;left:8px;top:8px;font-size:7px;font-weight:700;color:var(--light);white-space:nowrap}
.card .role{position:absolute;left:8px;top:17px;font-size:5px;color:#cfc6bd}
.card .info{position:absolute;left:8px;bottom:6px;font-size:4.5px;line-height:1.4;color:#cfc6bd;white-space:nowrap}
.card .center{position:absolute;inset:0;display:flex;align-items:center;justify-content:center}
.card .brand{font-size:10px}
.card .brand .dot{width:7px;height:7px}

/* letterheads */
.letter{width:186px;height:288px;top:12px;background:var(--paper);box-shadow:var(--shadow);overflow:hidden}
.letter .top-brand{position:absolute;left:0;width:130px;top:12px;display:flex;justify-content:center}
.letter .brand{font-size:8px;gap:4px}
.letter .brand .dot{width:5px;height:5px}
.letter .head-band{position:absolute;left:0;right:0;top:0;height:24px;background:var(--charcoal)}
.letter .head-band .brand{position:absolute;left:10px;top:8px}
.letter .contact{position:absolute;right:8px;top:7px;font-size:4px;line-height:1.4;text-align:right;color:#e2dad2;white-space:nowrap}
.letter .contact.dark{background:var(--charcoal);width:52px;padding:3px 4px;top:6px;right:0;text-align:left}
.letter .mark{position:absolute;left:50%;top:50%;width:110px;height:110px;margin:-75px 0 0 -55px;border-radius:50%;border:6px solid var(--faint)}
.letter .foot{position:absolute;left:0;right:0;bottom:8px;text-align:center;font-size:4px;color:#8c857f}

/* #10 envelopes */
.env-long{width:204px;height:86px;background:var(--paper);box-shadow:var(--shadow)}
.env-long .band{position:absolute;left:0;right:0;top:10px;height:16px;background:var(--charcoal)}
.env-long .brand{position:absolute;left:10px;top:14px;font-size:8px}
.env-long .brand .dot{width:6px;height:6px}
.env-long .ret{position:absolute;left:10px;top:30px;font-size:4px;line-height:1.4;color:var(--ink)}

/* right envelopes */
.env-beige{left:936px;top:98px;width:250px;height:84px;background:var(--beige);box-shadow:var(--shadow)}
.env-dark{left:928px;top:148px;width:250px;height:80px;background:var(--charcoal);box-shadow:var(--shadow)}
.env-open{left:920px;top:204px;width:250px;height:92px;background:var(--paper);box-shadow:var(--shadow)}
.env-open svg,.env-dark svg{position:absolute;left:0;top:0}
.env-beige .brand{position:absolute;left:12px;top:10px;font-size:8px}
.env-beige .brand .dot{width:6px;height:6px}
</style>
</head>
<body>
<main class="canvas">

  <section class="abs logo-block">
    <div class="brand"><span class="dot"></span>Brookhaven</div>
    <p class="tagline">PRIVATE CHEF &amp; CATERING</p>
  </section>

  <div class="abs card card-dark" style="left:18px;top:140px">
    <span class="name">Daniel Hensley</span>
    <span class="role">Chef/Owner</span>
    <div class="band"></div>
    <p class="info">dan@brookhavenkitchens.example<br>www.brookhavenkitchens.example</p>
  </div>
  <div class="abs card card-dark" style="left:132px;top:140px">
    <div class="band" style="top:0;height:14px"></div>
    <span class="name" style="top:22px">Brookhaven Kitchens</span>
    <p class="info">4738 W. Marlow Ave<br>Orlando, FL 32899<br>(407) 555-0148</p>
  </div>
  <div class="abs card card-dark" style="left:18px;top:222px">
    <div class="center"><div class="brand light"><span class="dot"></span>Brookhaven</div></div>
  </div>
  <div class="abs card card-rust" style="left:132px;top:222px">
    <div class="center"><div class="brand light"><span class="dot"></span>BK</div></div>
  </div>

  <article class="abs letter" style="left:264px">
    <div class="top-brand"><div class="brand"><span class="dot"></span>Brookhaven</div></div>
    <p class="contact dark">4738 W. Marlow Ave<br>Orlando, FL 32899<br>(407) 555-0148</p>
    <div class="mark" role="img" aria-label="Faint monogram circle"></div>
    <p class="foot">www.brookhavenkitchens.example</p>
  </article>

  <article class="abs letter" style="left:492px">
    <div class="head-band">
      <div class="brand light"><span class="dot"></span>Brookhaven</div>
      <p class="contact">dan@brookhavenkitchens.example<br>(407) 555-0148</p>
    </div>
    <div class="mark" role="img" aria-label="Faint monogram circle"></div>
    <p class="foot">4738 W. Marlow Ave Orlando, FL 32899</p>
  </article>

  <div class="abs env-long" style="left:700px;top:96px">
    <div class="band"></div>
    <div class="brand light"><span class="dot"></span>Brookhaven</div>
    <p class="ret">4738 W. Marlow Ave<br>Orlando, FL 32899</p>
  </div>
  <div class="abs env-long" style="left:700px;top:206px">
    <div class="band"></div>
    <div class="brand light"><span class="dot"></span>Brookhaven</div>
    <p class="ret">4738 W. Marlow Ave<br>Orlando, FL 32899</p>
  </div>

  <div class="abs env-beige">
    <div class="brand"><span class="dot"></span>Brookhaven</div>
  </div>
  <div class="abs env-dark">
    <svg width="250" height="80" viewBox="0 0 250 80"><polyline points="0,0 125,46 250,0" fill="none" stroke="#2c2a28" stroke-width="2"/><circle cx="125" cy="46" r="6" fill="var(--rust)"/></svg>
  </div>
  <div class="abs env-open">
    <svg width="250" height="92" viewBox="0 0 250 92"><polygon points="0,0 125,40 250,0" fill="var(--charcoal)"/><polyline points="0,92 125,50 250,92" fill="none" stroke="#dedad5" stroke-width="1"/></svg>
  </div>

</main>
</body>
</html>
```